a promotional poster design to promote our upcoming event. We want the date to be promoted as "Save the Date" for Sunday 4th July 2021.

Poster design

Requirements
Must have
• the following text;

Save the Date! (stand out)
Sunday 4th July 2021 (stand out)
KORB Family Mixed Netball Carnival
Nice to have
• make the date stand out. We want people to lock in the date we're promoting.

```html
<!DOCTYPE html>
<html lang="en">
<head>
<meta charset="utf-8">
<title>KORB Family Mixed Netball Carnival – Save the Date</title>
<link rel="stylesheet" href="https://fonts.googleapis.com/css2?family=Arimo:wght@400;700&display=swap">
<style>
  :root {
    --poster-red: #ec1c24;
    --ink-white: #ffffff;
    --ink-dark: #1a1a1a;
    --ball-light: rgba(255, 255, 255, 0.55);
    --ball-fade: rgba(255, 255, 255, 0);
    --streak-light: rgba(255, 150, 155, 0.55);
  }
  * { margin: 0; padding: 0; box-sizing: border-box; }
  html, body {
    width: 848px;
    height: 1200px;
    overflow: hidden;
    background: var(--poster-red);
  }
  .poster {
    position: relative;
    width: 848px;
    height: 1200px;
    background: var(--poster-red);
    font-family: "Arimo", Arial, sans-serif;
    color: var(--ink-white);
    overflow: hidden;
  }
  .poster-art {
    position: absolute;
    inset: 0;
    width: 848px;
    height: 1200px;
  }
  .poster-art text {
    font-family: "Arimo", Arial, sans-serif;
    fill: var(--ink-white);
  }
  .event-title { font-size: 58px; font-weight: 400; }
  .save-word { font-size: 170px; font-weight: 400; }
  .date-word { font-size: 88px; font-weight: 400; }

  .host-card {
    position: absolute;
    left: 323px;
    top: 981px;
    width: 198px;
    height: 198px;
    background: var(--ink-white);
    display: flex;
    flex-direction: column;
    align-items: center;
    justify-content: center;
    gap: 16px;
  }
  .host-mark {
    width: 58px;
    height: 58px;
    border-radius: 50%;
    background: var(--poster-red);
  }
  .host-name {
    font-family: "Arimo", Arial, sans-serif;
    font-weight: 700;
    font-size: 14px;
    line-height: 1.25;
    letter-spacing: 0.3px;
    text-transform: uppercase;
    text-align: center;
    color: var(--ink-dark);
  }
</style>
</head>
<body>
<main class="poster">
  <svg class="poster-art" width="848" height="1200" viewBox="0 0 848 1200" xmlns="http://www.w3.org/2000/svg">
    <defs>
      <radialGradient id="ball-glow" cx="0.5" cy="0.5" r="0.5">
        <stop offset="0" stop-color="#ffffff" stop-opacity="0.35"/>
        <stop offset="0.8" stop-color="#ffffff" stop-opacity="0.45"/>
        <stop offset="1" stop-color="#ffffff" stop-opacity="0"/>
      </radialGradient>
      <linearGradient id="streak-glow" x1="0" y1="0" x2="1" y2="1">
        <stop offset="0" stop-color="#ff9aa0" stop-opacity="0.5"/>
        <stop offset="1" stop-color="#ff9aa0" stop-opacity="0.1"/>
      </linearGradient>
    </defs>

    <!-- Event title -->
    <text class="event-title" x="436" y="145" text-anchor="middle" textLength="521" lengthAdjust="spacingAndGlyphs">KORB Family Mixed</text>
    <text class="event-title" x="418" y="199" text-anchor="middle" textLength="402" lengthAdjust="spacingAndGlyphs">Netball Carnival</text>
    <rect class="title-rule" x="83" y="243" width="683" height="7" fill="#ffffff"/>

    <!-- Save the date block -->
    <text class="save-word" x="83" y="477" textLength="359" lengthAdjust="spacingAndGlyphs">SAVE</text>
    <text class="save-word" x="173" y="619" textLength="269" lengthAdjust="spacingAndGlyphs">THE</text>
    <text class="save-word" x="87" y="763" textLength="355" lengthAdjust="spacingAndGlyphs">DATE</text>
    <rect class="divider-bar" x="477" y="355" width="13" height="408" fill="#ffffff"/>

    <!-- Event date -->
    <text class="date-word" x="525" y="481" textLength="241" lengthAdjust="spacingAndGlyphs">Sunday</text>
    <text class="date-word" x="592" y="580" textLength="120" lengthAdjust="spacingAndGlyphs">4th</text>
    <text class="date-word" x="561" y="646" textLength="156" lengthAdjust="spacingAndGlyphs">July</text>
    <text class="date-word" x="543" y="726" textLength="191" lengthAdjust="spacingAndGlyphs">2021</text>

    <!-- Decorative areas -->
    <rect class="court-streaks" role="img" aria-label="Flowing light streak pattern across the lower left" x="0" y="1024" width="324" height="176" fill="url(#streak-glow)"/>
    <circle class="netball-graphic" role="img" aria-label="Dotted illustration of a netball" cx="664" cy="1010" r="228" fill="url(#ball-glow)"/>
  </svg>

  <div class="host-card">
    <div class="host-mark"></div>
    <p class="host-name">Korbin Valley<br>Health Service</p>
  </div>
</main>
</body>
</html>
```